Bramblecove Suite Complementary Pass

I’d like a complimentary pass for any 30-minute Bramblecove Suite session. Choose one of the following options: Infrared Sauna with Red Light, Massage Chair Velquora Compression Therapy, or Paraffin Wax Hand Bath.

Please incorporate the logo and brand colors into your design. I’d like a square image that will be printed on square business cards (no rectangles).

Please refer to the logo and menu for more details.

Contact Information for Business Card

See discretion

```html
<!DOCTYPE html>
<html lang="en">
<head>
<meta charset="utf-8">
<title>Solvane Physical Therapy – Bramblecove Suite Pass</title>
<link href="https://fonts.googleapis.com/css2?family=Nunito:wght@500;600;700&family=Hind:wght@400;600&family=Oswald:wght@500&family=Allura&display=swap" rel="stylesheet">
<style>
  :root {
    --purple: #453387;
    --purple-light: #5b49a0;
    --orange: #ee6545;
    --navy: #3a2d88;
    --ink: #1e1b2e;
    --paper: #fdfdfd;
    --backdrop: #c3c4c6;
  }
  * { margin: 0; padding: 0; box-sizing: border-box; }
  html, body { width: 1200px; height: 900px; overflow: hidden; }
  body { background: var(--backdrop); position: relative; font-family: "Nunito", sans-serif; }

  .card { position: absolute; overflow: hidden; }

  /* Front */
  .card-front {
    left: 113px; top: 222px; width: 459px; height: 456px;
    border-radius: 60px; background: var(--purple);
  }
  .front-scene {
    position: absolute; left: 0; right: 0; bottom: 0; height: 260px;
    background: linear-gradient(180deg, rgba(91,73,160,0) 0%, rgba(91,73,160,0.55) 55%, rgba(110,92,175,0.75) 100%);
  }
  .front-mark {
    position: absolute; left: 50%; top: 118px; width: 58px; height: 58px;
    margin-left: -29px; border-radius: 50%; background: var(--orange);
  }
  .front-name {
    position: absolute; left: 0; right: 0; top: 200px; text-align: center;
    color: #fff; font-size: 84px; font-weight: 600; line-height: 1; letter-spacing: -1px;
  }
  .front-tagline {
    position: absolute; left: 0; right: 0; top: 332px; text-align: center;
    color: #fff; font-family: "Oswald", sans-serif; font-weight: 500;
    font-size: 27px; letter-spacing: 3.5px; line-height: 1;
  }

  /* Back */
  .card-back {
    left: 627px; top: 220px; width: 461px; height: 460px;
    border-radius: 46px; background: var(--paper); color: var(--navy);
  }
  .back-brand {
    position: absolute; left: 0; right: 0; top: 18px; text-align: center;
    font-size: 31px; font-weight: 600; color: var(--navy); line-height: 1;
  }
  .suite-title {
    position: absolute; left: 0; right: 0; top: 64px; text-align: center;
    font-family: "Allura", cursive; font-size: 52px; line-height: 1; color: var(--navy);
  }
  .pass-rule {
    position: absolute; left: 0; right: 0; top: 143px;
    display: flex; align-items: center; gap: 7px;
  }
  .pass-rule::before, .pass-rule::after { content: ""; flex: 1; height: 1px; background: var(--navy); }
  .pass-rule span { color: var(--orange); font-size: 13.5px; font-weight: 700; letter-spacing: .3px; }

  .service-list {
    position: absolute; left: 28px; top: 170px; list-style: none;
    font-family: "Hind", sans-serif; font-size: 13.5px; color: var(--ink); line-height: 18.7px;
  }
  .service-list li::before {
    content: ""; display: inline-block; width: 5px; height: 5px; border-radius: 50%;
    background: var(--navy); margin-right: 6px; vertical-align: 2px;
  }
  .price-row {
    position: absolute; left: 234px; right: 27px;
    font-family: "Hind", sans-serif; font-size: 13px; font-style: italic; font-weight: 600; color: var(--ink);
    display: flex; justify-content: space-between;
  }
  .price-row .amount { font-style: normal; font-weight: 600; color: var(--navy); }
  .price-row .note { font-weight: 400; margin-left: 36px; }

  .person-name {
    position: absolute; left: 0; right: 0; top: 262px; text-align: center;
    color: var(--orange); font-size: 24px; font-weight: 600; letter-spacing: 1.5px;
  }
  .person-role {
    position: absolute; left: 0; right: 0; top: 294px; text-align: center;
    font-size: 15px; letter-spacing: 1px; line-height: 18px; color: var(--navy);
  }
  .role-rule { position: absolute; left: 179px; width: 102px; top: 336px; height: 2px; background: var(--orange); }

  .contact-list { position: absolute; left: 28px; top: 351px; list-style: none; font-size: 15px; line-height: 21.5px; }
  .contact-list li { display: flex; align-items: center; gap: 8px; }
  .contact-list svg { width: 13px; height: 13px; fill: var(--orange); flex: none; }
  .contact-list .phone { letter-spacing: 3px; }

  .clinic {
    position: absolute; right: 28px; top: 349px; text-align: right; font-size: 15px; line-height: 20.5px;
  }
  .clinic-label { color: var(--orange); font-weight: 700; font-size: 17px; line-height: 22px; margin-bottom: 2px; }

  .back-band {
    position: absolute; left: 0; right: 0; bottom: 0; height: 34px; background: var(--purple);
    display: flex; align-items: center; justify-content: center;
    color: #fff; font-size: 15px; font-weight: 600;
  }
</style>
</head>
<body>

<section class="card card-front">
  <div class="front-scene" role="img" aria-label="Purple-tinted photo of a wooden boardwalk winding through tall grasses"></div>
  <div class="front-mark"></div>
  <div class="front-name">solvane</div>
  <div class="front-tagline">PHYSICAL THERAPY</div>
</section>

<section class="card card-back">
  <div class="back-brand">solvane</div>
  <h1 class="suite-title">Bramblecove Suite</h1>
  <div class="pass-rule"><span>Complimentary Pass for any 30-minute</span></div>

  <ul class="service-list">
    <li>Infrared Sauna + Red Light</li>
    <li>Velquora Compression</li>
    <li>Massage Chair</li>
    <li>Paraffin Wax Hand Bath</li>
  </ul>

  <div class="price-row" style="top:182px"><span>Any 30 min session</span><span class="amount">$40</span></div>
  <div class="price-row" style="top:200px"><span>Any 60 min session</span><span class="amount">$65</span></div>
  <div class="price-row" style="top:226px"><span class="note">(15 minutes)</span><span class="amount">$25</span></div>

  <div class="person-name">Corinne Halvorsen</div>
  <div class="person-role">Dr. Physical Therapy<br>Clinic Director</div>
  <div class="role-rule"></div>

  <ul class="contact-list">
    <li>
      <svg viewBox="0 0 24 24" aria-hidden="true"><path d="M6.6 10.8a15.1 15.1 0 0 0 6.6 6.6l2.2-2.2c.3-.3.7-.4 1-.2 1.1.4 2.3.6 3.6.6.6 0 1 .4 1 1V20c0 .6-.4 1-1 1A17 17 0 0 1 3 4c0-.6.4-1 1-1h3.5c.6 0 1 .4 1 1 0 1.3.2 2.5.6 3.6.1.3 0 .7-.2 1z"/></svg>
      <span class="phone">555-014-2290</span>
    </li>
    <li>
      <svg viewBox="0 0 24 24" aria-hidden="true"><path d="M2 5h20v14H2z M2 5l10 8 10-8" stroke="#fff" stroke-width="1.5"/></svg>
      <span>office@solvaneptclinic.com</span>
    </li>
    <li>
      <svg viewBox="0 0 24 24" aria-hidden="true"><path d="M12 2a10 10 0 1 0 0 20 10 10 0 0 0 0-20zm6.9 6h-3a15.6 15.6 0 0 0-1.3-3.6A8 8 0 0 1 18.9 8zM12 4c.8 1.2 1.5 2.5 1.9 4h-3.8c.4-1.5 1.1-2.8 1.9-4zM4.3 14a8 8 0 0 1 0-4h3.4a16 16 0 0 0 0 4zm.8 2h3a15.6 15.6 0 0 0 1.3 3.6A8 8 0 0 1 5.1 16zm3-8h-3a8 8 0 0 1 4.3-3.6C8.8 5.5 8.4 6.7 8.1 8zM12 20c-.8-1.2-1.5-2.5-1.9-4h3.8c-.4 1.5-1.1 2.8-1.9 4zm2.3-6H9.7a14 14 0 0 1 0-4h4.6a14 14 0 0 1 0 4zm.3 5.6c.6-1.1 1-2.3 1.3-3.6h3a8 8 0 0 1-4.3 3.6zm1.7-5.6a16 16 0 0 0 0-4h3.4a8 8 0 0 1 0 4z"/></svg>
      <span>solvaneptclinic.com</span>
    </li>
  </ul>

  <address class="clinic" style="font-style:normal">
    <div class="clinic-label">Clinic</div>
    418 Alder Street Suite 210<br>
    Millbrook, Oregon 97000
  </address>

  <div class="back-band">solvane</div>
</section>

</body>
</html>
```